Digital & Print Graphic Design templates for Comedy Club

We need new new digital & print graphic design templates for our upcoming comedy events created for use in CRAFTLY in the following specs
Digital:
1080x1080px
1200x600px
800x400px
1920x1080px
1080x1355px
1500x500px
851x315px
Print
11x17"
22x28"
95.5x30"

Target Market(s)

18+ comedy fans

Industry/Entity Type

comedy club

Font styles to use
Sans Serif

Colors
FFF300
FFF600
FEFA6F
FFFEC7
FFFEE8
6B429C
8869AF
B7A5CE
E3DAEB
F3F0F8

Requirements
Must have
• templates must be CRAFTLY compatible. frame for comedian photo.
Nice to have
• would like to incorporate deep purple into the design
Should not have
• do not include phone number on any templates

```html
<!DOCTYPE html>
<html lang="en">
<head>
<meta charset="utf-8">
<title>Grin Room – Comedy Event Templates</title>
<link href="https://fonts.googleapis.com/css2?family=Bebas+Neue&family=Montserrat:wght@500;600;700&family=Roboto:wght@500&display=swap" rel="stylesheet">
<style>
  :root{
    --yellow:#FFF300;
    --yellow-soft:#FEFA6F;
    --purple:#6B429C;
    --purple-mid:#8869AF;
    --lilac:#B7A5CE;
    --lavender:#E3DAEB;
    --mist:#F3F0F8;
    --board:#EFE6FC;
    --ink:#35206E;
    --teal-box:#2F5A55;
    --night-box:#2B2350;
  }
  *{box-sizing:border-box;margin:0;padding:0}
  html,body{width:1200px;height:703px;overflow:hidden;background:var(--board)}
  .board{position:relative;width:1200px;height:703px}

  .banner{position:absolute;background:var(--purple);overflow:hidden;box-shadow:0 24px 40px rgba(90,70,130,.28)}
  .kicker{position:absolute;font-family:'Montserrat',sans-serif;font-weight:600;color:var(--lilac);letter-spacing:.04em;white-space:nowrap}
  .title{position:absolute;font-family:'Bebas Neue',sans-serif;color:var(--yellow);line-height:.92;white-space:nowrap}
  .date{position:absolute;font-family:'Montserrat',sans-serif;font-weight:700;color:#fff;line-height:1;white-space:nowrap}
  .frame-accent{position:absolute;background:var(--yellow)}
  .frame-backing{position:absolute;background:#fff}
  .photo{position:absolute;background:linear-gradient(180deg,var(--mist) 0%,#ead9cc 38%,#c9a48c 55%,#8cc4bf 72%,#6fa9a3 100%)}

  .club-name{position:absolute;display:flex;flex-direction:column;align-items:center;gap:.25em;font-family:'Montserrat',sans-serif;font-weight:700;line-height:1;text-align:center;color:var(--yellow);white-space:nowrap}
  .club-name::before{content:"";width:.7em;height:.7em;border-radius:50%;background:currentColor}
  .club-name.on-photo{color:var(--ink)}

  .web{position:absolute;font-family:'Montserrat',sans-serif;font-weight:600;white-space:nowrap}

  .caption{position:absolute;left:0;width:1200px;top:624px;text-align:center;font-family:'Roboto',sans-serif;font-weight:500;font-size:31px;color:var(--ink)}
</style>
</head>
<body>
<main class="board">

  <!-- Square 1080x1080 -->
  <section class="banner" style="left:84px;top:94px;width:165px;height:165px">
    <p class="kicker" style="left:0;width:165px;text-align:center;top:7px;font-size:4px">LIVE AT COMEDY</p>
    <h2 class="title" style="left:12px;top:14px;font-size:33px">DAN MARLOW</h2>
    <div class="frame-accent" style="left:132px;top:46px;width:26px;height:130px;transform:rotate(3deg)"></div>
    <div class="frame-backing" style="left:58px;top:44px;width:92px;height:130px;transform:rotate(2deg)"></div>
    <div class="photo" role="img" aria-label="Comedian headshot photo" style="left:62px;top:48px;width:90px;height:120px"></div>
    <p class="date" style="left:14px;top:63px;font-size:11px;text-align:center;line-height:1.3">FEB<br>4</p>
    <p class="club-name" style="left:8px;top:110px;width:48px;font-size:10px">GRIN<br>ROOM</p>
  </section>

  <!-- Wide 1200x600 -->
  <section class="banner" style="left:274px;top:94px;width:290px;height:165px">
    <p class="kicker" style="left:36px;top:13px;font-size:4.5px">LIVE COMEDY EVENT</p>
    <h2 class="title" style="left:22px;top:34px;font-size:44px;text-align:center;width:120px">THEO<br>BRANDT</h2>
    <p class="date" style="left:40px;width:100px;text-align:center;top:136px;font-size:13px;font-weight:600">April 3-4</p>
    <div class="frame-accent" style="left:146px;top:-6px;width:120px;height:180px;transform:rotate(4deg)"></div>
    <div class="frame-backing" style="left:166px;top:0;width:118px;height:175px;transform:rotate(5deg);background:var(--teal-box)"></div>
    <div class="photo" role="img" aria-label="Comedian headshot photo" style="left:142px;top:10px;width:148px;height:155px;background:linear-gradient(180deg,transparent 0%,#c9a48c 45%,#8cc4bf 70%,#6fa9a3 100%)"></div>
    <p class="club-name on-photo" style="left:226px;top:118px;width:52px;font-size:10px">GRIN<br>ROOM</p>
  </section>

  <!-- Portrait 1080x1355 -->
  <section class="banner" style="left:84px;top:272px;width:165px;height:205px">
    <p class="kicker" style="left:0;width:165px;text-align:center;top:11px;font-size:4px">LIVE AT COMEDY</p>
    <h2 class="title" style="left:12px;top:20px;font-size:33px">DAN MARLOW</h2>
    <p class="date" style="right:14px;top:53px;font-size:7px;font-weight:600">February 4</p>
    <div class="frame-accent" style="left:40px;top:66px;width:120px;height:150px;transform:rotate(-3deg)"></div>
    <div class="frame-backing" style="left:32px;top:70px;width:122px;height:150px;transform:rotate(-3deg)"></div>
    <div class="photo" role="img" aria-label="Comedian headshot photo" style="left:36px;top:80px;width:129px;height:125px"></div>
    <p class="club-name on-photo" style="left:40px;top:162px;width:48px;font-size:10px">GRIN<br>ROOM</p>
  </section>

  <!-- Facebook cover 851x315 -->
  <section class="banner" style="left:274px;top:272px;width:227px;height:76px">
    <p class="kicker" style="left:18px;top:4px;font-size:3px">LIVE AT COMEDY</p>
    <h2 class="title" style="left:8px;top:12px;font-size:27px;text-align:center;width:76px">DAN<br>MARLOW</h2>
    <p class="date" style="left:22px;top:66px;font-size:5px;font-weight:600">February 4</p>
    <div class="frame-accent" style="left:86px;top:-4px;width:82px;height:86px;transform:rotate(3deg)"></div>
    <div class="frame-backing" style="left:92px;top:0;width:76px;height:80px;background:var(--night-box)"></div>
    <div class="photo" role="img" aria-label="Comedian headshot photo" style="left:92px;top:6px;width:74px;height:70px;background:linear-gradient(180deg,transparent 0%,#c9a48c 45%,#8cc4bf 70%,#6fa9a3 100%)"></div>
    <p class="club-name" style="left:172px;top:20px;width:48px;font-size:9px">GRIN<br>ROOM</p>
    <p class="web" style="left:170px;top:64px;font-size:3.5px;color:var(--lilac)">grinroomclub.com</p>
  </section>

  <!-- Small web banner 800x400 -->
  <section class="banner" style="left:274px;top:368px;width:122px;height:61px">
    <h2 class="title" style="left:5px;top:9px;font-size:17px;text-align:center;width:58px">RUDI<br>VARGA</h2>
    <p class="date" style="left:9px;top:50px;font-size:4px;font-weight:600;color:var(--lilac)">January 20-21</p>
    <div class="frame-accent" style="left:60px;top:2px;width:44px;height:62px;transform:rotate(-4deg)"></div>
    <div class="frame-backing" style="left:64px;top:6px;width:46px;height:58px;transform:rotate(-3deg)"></div>
    <div class="photo" role="img" aria-label="Comedian headshot photo" style="left:66px;top:12px;width:44px;height:49px"></div>
    <p class="club-name on-photo" style="left:94px;top:42px;width:22px;font-size:4.5px">GRIN<br>ROOM</p>
  </section>

  <!-- Twitter header 1500x500 -->
  <section class="banner" style="left:84px;top:492px;width:131px;height:50px">
    <h2 class="title" style="left:3px;top:6px;font-size:16px;text-align:center;width:48px">KIP<br>DORRAN</h2>
    <div class="frame-accent" style="left:48px;top:-2px;width:50px;height:56px;transform:rotate(-4deg)"></div>
    <div class="frame-backing" style="left:56px;top:2px;width:44px;height:50px;transform:rotate(-3deg)"></div>
    <div class="photo" role="img" aria-label="Comedian headshot photo" style="left:58px;top:6px;width:42px;height:44px"></div>
    <p class="club-name" style="left:102px;top:14px;width:26px;font-size:5.5px">GRIN<br>ROOM</p>
  </section>

  <!-- HD 1920x1080 -->
  <section class="banner" style="left:274px;top:449px;width:181px;height:93px">
    <p class="kicker" style="left:24px;top:9px;font-size:3px">LIVE AT COMEDY</p>
    <h2 class="title" style="left:6px;top:17px;font-size:25px;text-align:center;width:76px">DAN<br>MARLOW</h2>
    <p class="date" style="left:22px;top:78px;font-size:4.5px;font-weight:600">February 4</p>
    <div class="frame-accent" style="left:82px;top:-4px;width:80px;height:100px;transform:rotate(-3deg)"></div>
    <div class="frame-backing" style="left:90px;top:2px;width:76px;height:96px;transform:rotate(-2deg)"></div>
    <div class="photo" role="img" aria-label="Comedian headshot photo" style="left:92px;top:6px;width:76px;height:87px"></div>
    <p class="club-name on-photo" style="left:144px;top:58px;width:28px;font-size:6px">GRIN<br>ROOM</p>
    <p class="web" style="left:118px;top:86px;font-size:3.5px;color:var(--yellow)">grinroomclub.com</p>
  </section>

  <!-- Poster 11x17 -->
  <section class="banner" style="left:622px;top:94px;width:227px;height:290px">
    <p class="kicker" style="left:0;width:227px;text-align:center;top:14px;font-size:6px">LIVE AT COMEDY</p>
    <h2 class="title" style="left:0;width:227px;text-align:center;top:22px;font-size:56px">KIP DORRAN</h2>
    <div class="frame-accent" style="left:78px;top:80px;width:150px;height:220px;transform:rotate(-5deg)"></div>
    <div class="frame-backing" style="left:86px;top:84px;width:150px;height:215px;transform:rotate(3deg)"></div>
    <div class="photo" role="img" aria-label="Comedian headshot photo" style="left:82px;top:92px;width:145px;height:175px"></div>
    <div class="web" style="left:86px;top:266px;width:141px;height:18px;background:#fff;color:var(--purple);font-size:6.5px;display:flex;align-items:center;justify-content:center">grinroomclub.com</div>
    <p class="date" style="left:14px;top:118px;font-size:27px;line-height:1.02">Feb<br>4-7</p>
    <p class="club-name" style="left:10px;top:214px;width:60px;font-size:13px">GRIN<br>ROOM</p>
  </section>

  <!-- Poster 22x28 -->
  <section class="banner" style="left:874px;top:96px;width:139px;height:216px">
    <h2 class="title" style="left:6px;top:10px;font-size:28px">SAM HOLT</h2>
    <p class="date" style="left:10px;top:40px;font-size:7.5px;font-weight:600;color:var(--lavender)">March 6-7</p>
    <div class="frame-accent" style="left:20px;top:58px;width:116px;height:170px;transform:rotate(-3deg)"></div>
    <div class="frame-backing" style="left:28px;top:62px;width:114px;height:160px;transform:rotate(2deg);background:var(--lavender)"></div>
    <div class="photo" role="img" aria-label="Comedian headshot photo" style="left:30px;top:68px;width:109px;height:128px;background:linear-gradient(180deg,var(--lavender) 0%,#ead9cc 38%,#c9a48c 55%,#8cc4bf 72%,#6fa9a3 100%)"></div>
    <div class="web" style="left:28px;top:198px;width:105px;height:12px;background:#fff;color:var(--purple);font-size:4px;display:flex;align-items:center;justify-content:center">grinroomclub.com</div>
    <p class="club-name on-photo" style="left:34px;top:152px;width:40px;font-size:9px">GRIN<br>ROOM</p>
  </section>

  <!-- Large banner 95.5x30 -->
  <section class="banner" style="left:622px;top:399px;width:494px;height:155px">
    <p class="kicker" style="left:40px;top:12px;font-size:5.5px">LIVE AT COMEDY</p>
    <h2 class="title" style="left:12px;top:24px;font-size:60px;text-align:center;width:160px">DAN<br>MARLOW</h2>
    <p class="date" style="left:45px;top:134px;font-size:12px;font-weight:600">February 4</p>
    <div class="frame-accent" style="left:184px;top:-6px;width:188px;height:170px;transform:rotate(-3deg)"></div>
    <div class="frame-backing" style="left:190px;top:-4px;width:176px;height:166px;transform:rotate(2deg);background:var(--mist)"></div>
    <div class="photo" role="img" aria-label="Comedian headshot photo" style="left:194px;top:8px;width:170px;height:147px"></div>
    <p class="club-name" style="left:380px;top:36px;width:76px;font-size:18px">GRIN<br>ROOM</p>
    <p class="web" style="left:378px;top:132px;font-size:6px;color:var(--lavender)">grinroomclub.com</p>
  </section>

  <p class="caption">Designed compatible with Craftly</p>
</main>
</body>
</html>
```